Plumbing Company business card design

Create a business card for our plumbing company. Following info needs to be present

Website-rivertoptapworks.net
Email- rivertoptapworks@mailnest.net
Phone-555-314-2098
Address-4876 NW Larkspur Blvd STE K
Maplecrest, Northland 50999

```html
<!DOCTYPE html>
<html lang="en">
<head>
<meta charset="utf-8">
<title>Rivertop Tapworks – Business Card</title>
<link rel="stylesheet" href="https://fonts.googleapis.com/css2?family=Open+Sans:wght@400;700;800&display=swap">
<style>
  :root {
    --backdrop: #4a4a4a;
    --card: #181818;
    --edge-blue: #0b4f9e;
    --brand-red: #ee2a2a;
    --brand-blue: #0b55a3;
    --ink-white: #f4f4f4;
  }
  * { box-sizing: border-box; margin: 0; padding: 0; }
  html, body {
    width: 1200px; height: 801px; overflow: hidden;
    background: var(--backdrop);
    font-family: "Open Sans", Arial, sans-serif;
  }
  .stage {
    position: relative; width: 1200px; height: 801px;
    display: flex; align-items: center; justify-content: center; gap: 40px;
  }
  .card {
    position: relative; width: 540px; height: 309px;
    background: var(--card);
    border-radius: 18px;
    border-bottom: 3px solid var(--edge-blue);
    overflow: hidden;
  }
  /* front */
  .card-front .wordmark {
    position: absolute; left: 34px; top: 40px;
    font-weight: 800; font-size: 22px; letter-spacing: 1px;
    text-transform: uppercase; color: var(--brand-red);
  }
  .card-front .company {
    position: absolute; left: 34px; top: 104px;
    font-weight: 700; font-size: 19px; color: var(--brand-red);
  }
  .contact-list {
    position: absolute; left: 34px; top: 148px;
    list-style: none; color: var(--ink-white); font-size: 13.5px; line-height: 22px;
  }
  .contact-list li { display: flex; align-items: center; gap: 9px; }
  .contact-list svg { width: 13px; height: 13px; flex: none; }
  .address {
    position: absolute; left: 34px; top: 226px;
    color: var(--ink-white); font-size: 13.5px; line-height: 21px; font-style: normal;
  }
  .front-mark {
    position: absolute; right: 40px; top: 62px;
    width: 184px; height: 184px;
    border-radius: 50%;
    background: var(--brand-blue);
  }
  /* back */
  .card-back .lockup {
    position: absolute; inset: 0;
    display: flex; flex-direction: column; align-items: center; justify-content: center; gap: 18px;
  }
  .card-back .lockup-dot {
    width: 80px; height: 80px; border-radius: 50%;
    background: var(--brand-blue);
  }
  .card-back .wordmark {
    font-weight: 800; font-size: 34px; letter-spacing: 2px;
    text-transform: uppercase; color: var(--brand-red);
  }
</style>
</head>
<body>
<main class="stage">
  <section class="card card-front">
    <div class="wordmark">Rivertop Tapworks</div>
    <h1 class="company">Rivertop Tapworks</h1>
    <ul class="contact-list">
      <li>
        <svg viewBox="0 0 16 16" aria-hidden="true"><path fill="var(--brand-red)" d="M3 1h3l1.5 4-2 1.3a9 9 0 0 0 4.2 4.2L11 8.5l4 1.5v3a2 2 0 0 1-2 2A12 12 0 0 1 1 3a2 2 0 0 1 2-2z"/></svg>
        555-314-2098
      </li>
      <li>
        <svg viewBox="0 0 16 16" aria-hidden="true"><rect x="1" y="3" width="14" height="10" rx="1.5" fill="var(--brand-red)"/><path d="M1.5 4l6.5 5 6.5-5" stroke="var(--card)" stroke-width="1.4" fill="none"/></svg>
        rivertoptapworks@mailnest.net
      </li>
      <li>
        <svg viewBox="0 0 16 16" aria-hidden="true"><circle cx="8" cy="8" r="6.5" fill="none" stroke="var(--brand-red)" stroke-width="1.6"/><path d="M1.5 8h13M8 1.5c-3 3.5-3 9.5 0 13M8 1.5c3 3.5 3 9.5 0 13" stroke="var(--brand-red)" stroke-width="1.2" fill="none"/></svg>
        www.rivertoptapworks.net
      </li>
    </ul>
    <address class="address">
      4876 NW Larkspur Blvd STE K<br>Maplecrest, Northland 50999
    </address>
    <div class="front-mark" aria-hidden="true"></div>
  </section>

  <section class="card card-back">
    <div class="lockup">
      <div class="lockup-dot" aria-hidden="true"></div>
      <div class="wordmark">Rivertop Tapworks</div>
    </div>
  </section>
</main>
</body>
</html>
```